Need a business card for a Construction and Remodeling company.
Our company logo is the fleur de lis design as thats the family crust that we use on our logos.
Heres the info it needs:

Brackmore Construction & Remodeling, LLC
Renovations * Restorations

Elwin R. Brackmore
845 North Quarry Road
Ashbrook Connecticut 06488
(203) 555.0182
CT LIC/REG: 418257

home owners, customers

```html
<!DOCTYPE html>
<html lang="en">
<head>
<meta charset="utf-8">
<title>Brackmore Construction &amp; Remodeling — Business Card</title>
<link rel="stylesheet" href="https://fonts.googleapis.com/css2?family=Montserrat:wght@500;600;700&display=swap">
<style>
  :root {
    --page-bg: #ffffff;
    --card-bg: #ffffff;
    --card-edge: #2b2b2b;
    --brand-navy: #27338c;
    --band-dark: #2f4284;
    --band-mid: #4a62a6;
    --band-light: #6b80bb;
    --on-band: #ffffff;
  }
  * { margin: 0; padding: 0; box-sizing: border-box; }
  html, body {
    width: 1200px;
    height: 800px;
    overflow: hidden;
    background: var(--page-bg);
  }
  .canvas {
    position: relative;
    width: 1200px;
    height: 800px;
  }
  .business-card {
    position: absolute;
    left: 150px;
    top: 150px;
    width: 900px;
    height: 500px;
    background: var(--card-bg);
    border: 2px solid var(--card-edge);
    overflow: hidden;
    font-family: "Montserrat", sans-serif;
  }
  .brand-band {
    position: absolute;
    left: 0;
    top: 0;
    width: 100%;
    height: 267px;
    background:
      radial-gradient(ellipse at 70% 40%, var(--band-light) 0%, transparent 55%),
      linear-gradient(135deg, var(--band-mid) 0%, var(--band-dark) 55%, var(--band-mid) 100%);
  }
  .brand-mark {
    position: absolute;
    left: 0;
    top: 0;
    width: 100%;
    height: 267px;
    display: flex;
    align-items: center;
    justify-content: center;
    gap: 28px;
    padding-right: 40px;
  }
  .brand-dot {
    width: 96px;
    height: 96px;
    border-radius: 50%;
    background: var(--on-band);
    flex: none;
  }
  .brand-name {
    color: var(--on-band);
    font-weight: 600;
    font-size: 38px;
    line-height: 1.22;
    letter-spacing: 0.2px;
  }
  .contact-area {
    position: absolute;
    left: 0;
    top: 267px;
    width: 100%;
    height: 233px;
  }
  .person-name {
    position: absolute;
    right: 598px;
    top: 55px;
    text-align: right;
    color: var(--brand-navy);
    font-weight: 700;
    font-size: 42px;
    line-height: 1.12;
    white-space: nowrap;
  }
  .divider {
    position: absolute;
    left: 342px;
    top: 26px;
    width: 4px;
    height: 180px;
    background: var(--brand-navy);
  }
  .contact-lines {
    position: absolute;
    left: 383px;
    top: 33px;
    list-style: none;
    color: var(--brand-navy);
    font-weight: 500;
    font-size: 28px;
    line-height: 42px;
    white-space: nowrap;
  }
</style>
</head>
<body>
<main class="canvas">
  <article class="business-card">
    <div class="brand-band" role="img" aria-label="Blue-toned photograph of construction tools resting on architectural blueprints"></div>
    <div class="brand-mark">
      <span class="brand-dot" aria-hidden="true"></span>
      <p class="brand-name">Brackmore Construction<br>&amp; Remodeling, LLC.</p>
    </div>
    <section class="contact-area">
      <h1 class="person-name">Elwin R.<br>Brackmore</h1>
      <span class="divider" aria-hidden="true"></span>
      <ul class="contact-lines">
        <li>845 North Quarry Road, 06488</li>
        <li>Ashbrook, Connecticut</li>
        <li>(203) 555.0182</li>
        <li>CT LIC/REG: 418257</li>
      </ul>
    </section>
  </article>
</main>
</body>
</html>
```